Hollow Lantern Distillery

I need a label designed for my small distillery. I’d like it to have a rose, and the name hollow lantern in script writing. I need the graphic to fit a standard gin bottle and I’ll need to be able to edit it depending on alcohol, warning and descriptions. I want it to look elegant and attractive, but slightly daring too. It’s a 700ml oslo bottle
Target Market(s)
Bespoke gin and vodka drinkers
Industry/Entity Type
Beverage
Font styles to use
Script
Other font styles liked:
- Something easy to read
Requirements
Must have
- Room for me to add and remove text depending on the drink
Nice to have
- Hollow lantern in script, slight colour on the rose and black writing

```html
<!DOCTYPE html>
<html lang="en">
<head>
<meta charset="utf-8">
<title>Hollow Lantern Gin – Label</title>
<link rel="stylesheet" href="https://fonts.googleapis.com/css2?family=Pinyon+Script&family=Oswald:wght@200&display=swap">
<style>
  :root {
    --page-bg: #ffffff;
    --label-edge: #e2e2e2;
    --label-centre: #f7f7f7;
    --ink: #111111;
    --ink-soft: #3a3a3a;
    --rose-red: #d8372c;
    --rose-deep: #a82a22;
    --band-teal: #2f706c;
  }
  * { margin: 0; padding: 0; box-sizing: border-box; }
  html, body {
    width: 1200px;
    height: 1200px;
    overflow: hidden;
    background: var(--page-bg);
  }
  .canvas {
    position: relative;
    width: 1200px;
    height: 1200px;
  }
  .label {
    position: absolute;
    left: 100px;
    top: 90px;
    width: 1000px;
    height: 1020px;
    overflow: hidden;
  }
  .label__knotwork {
    position: absolute;
    inset: 0;
    background: radial-gradient(ellipse at 50% 50%, var(--label-centre) 0%, var(--label-centre) 40%, var(--label-edge) 100%);
  }
  .label__emblem {
    position: absolute;
    left: 232px;
    top: 244px;
    width: 551px;
    height: 442px;
    background:
      radial-gradient(ellipse 42% 44% at 50% 48%, var(--rose-red) 0%, var(--rose-deep) 60%, transparent 100%),
      linear-gradient(to right, transparent 0 30%, var(--band-teal) 30% 70%, transparent 70% 100%);
  }
  .label__name {
    position: absolute;
    font-family: "Pinyon Script", cursive;
    font-weight: 400;
    color: var(--ink);
    line-height: 1;
    white-space: nowrap;
  }
  .label__name--first {
    left: 290px;
    top: 150px;
    font-size: 84px;
  }
  .label__name--second {
    left: 230px;
    top: 680px;
    font-size: 84px;
  }
  .label__spirit {
    position: absolute;
    left: 0;
    right: 0;
    top: 850px;
    text-align: center;
    font-family: "Oswald", sans-serif;
    font-weight: 200;
    font-size: 104px;
    line-height: 1;
    color: var(--ink-soft);
    letter-spacing: 2px;
  }
</style>
</head>
<body>
  <main class="canvas">
    <section class="label">
      <div class="label__knotwork" role="img" aria-label="Faint grey interlaced knotwork pattern covering the label"></div>
      <div class="label__emblem" role="img" aria-label="Red rose with green leaves over a vertical teal band"></div>
      <p class="label__name label__name--first">Hollow</p>
      <p class="label__name label__name--second">Lantern</p>
      <p class="label__spirit">GIN</p>
    </section>
  </main>
</body>
</html>
```